Pest Control / Exterminator Banner Ads
Find local exterminators in your area
Dusk - #25 & #26 are excellent revisions of your original. I am not sure which one I like better Red or Blue. Excellent work.
Marlowe - I like 19 & 20 can you add all the sizes requested so I can get a look at all of the ads together.
#14 - I like the design of the banners with the ant, but the rodent and tarantula pictures are a little much. I would stick to pictures of termites, bed bugs, or you could use general pictures of a home or family.
#11 - Very good adjustment duskcraft! I like the bigger ads a lot, but the smaller ones I think need some adjustment. Because there is not a lot of room to get the point across, I would get rid of the logo for the box ads and replace with stronger call to action language or graphics. Branding is not as important as attention getting call to action to get a quote, or find a provider.
#4, #5 - This is not what we are looking for...It doesn't look like an ad that someone with a pest problem would click on? Maybe use some better graphics, like a home or a pest control technician?
BrightQuillWorks - We are not bugbanishcrew.example, I only submitted that site to give you an idea of other pest control display ads, our website is locatebughelpers.example, please see that site for additional design ideas.
#3 - Not sure what that is?
Duskcraft - We are not Vexaline. I only added those in the proposal as a guideline or example to build from. Our website is www.locatebughelpers.example and has nothing to do with Vexaline.

```html
<!DOCTYPE html>
<html lang="en">
<head>
<meta charset="utf-8">
<title>Bug Helpers Hub – Exterminator Banner Ads</title>
<link rel="stylesheet" href="https://fonts.googleapis.com/css2?family=Arimo:wght@400;700&display=swap">
<style>
:root{
  --stage:#3a3a3a;
  --brand-green:#4e8f22;
  --brand-blue:#1d5c9e;
  --deep-blue:#123f73;
  --bar-blue:#1f5f9a;
  --ink:#ffffff;
  --panel:#eef1f4;
  --cta-red:#d8321c;
  --cta-orange:#f07d18;
  --cta-yellow:#f6c51c;
  --badge-gold:#e3a51a;
  --skin:#c9a68c;
  --shirt:#7a6a5c;
  --backdrop:#d9d6d2;
  --critter:#6b4a32;
  --photo-sky:#9cc0dc;
  --lawn:#6f8a55;
}
*{box-sizing:border-box;margin:0;padding:0}
html,body{width:1200px;height:799px;overflow:hidden}
body{background:var(--stage);font-family:"Arimo",Arial,sans-serif;position:relative}
.ad{position:absolute;background:var(--panel);overflow:hidden;border:2px solid #fff}
.fill{position:absolute}
.photo-person{background:linear-gradient(180deg,var(--backdrop) 0%,var(--backdrop) 18%,var(--skin) 35%,var(--skin) 62%,var(--shirt) 78%,var(--shirt) 100%)}
.photo-critters{background:radial-gradient(ellipse at 30% 55%,var(--critter) 0 12%,transparent 13%),radial-gradient(ellipse at 70% 40%,#8c8580 0 16%,transparent 17%),linear-gradient(#eef1f4,#cfc8c0)}
.logo{position:absolute;background:#fff;display:flex;align-items:center;justify-content:center;gap:6px}
.logo .wordmark{color:var(--brand-green);font-weight:700;line-height:1.05;text-align:center;white-space:nowrap}
.logo .mark{width:10px;height:10px;background:var(--brand-blue);flex:none}
.url-bar{position:absolute;background:var(--bar-blue);color:var(--ink);font-weight:700;display:flex;align-items:center;justify-content:center;white-space:nowrap}
.headline{position:absolute;font-weight:700;text-transform:uppercase;line-height:1.05;text-align:center;color:var(--brand-blue)}
.headline small{display:block;text-transform:none;font-size:.6em}
.btn{position:absolute;font-weight:700;text-align:center;display:flex;flex-direction:column;align-items:center;justify-content:center;line-height:1.05}

/* skyscraper */
.sky{left:19px;top:19px;width:204px;height:766px}
.sky .headline{left:6px;right:6px;top:166px;font-size:24px;text-transform:none}
.sky .btn{left:12px;right:12px;top:450px;height:92px;background:var(--cta-red);color:#fff;font-size:26px;border-radius:6px;border:2px solid #fff}
.sky .tagline{position:absolute;left:4px;right:4px;top:676px;text-align:center;font-weight:700;line-height:1.15;color:var(--brand-blue);font-size:18px;white-space:nowrap}
.sky .tagline span{display:block;font-size:15px}

/* leaderboard */
.leader{left:240px;top:19px;width:941px;height:144px}
.leader .get-fast{position:absolute;left:590px;top:100px;width:136px;height:40px;background:var(--brand-blue);color:#fff;font-weight:700;font-size:20px;display:flex;align-items:center;justify-content:center;white-space:nowrap}
.leader .free{left:730px;top:100px;width:207px;height:40px;background:var(--cta-orange);color:#fff;flex-direction:row;gap:8px;font-size:24px}
.leader .free span{font-size:12px;line-height:1.1;text-align:left}

/* middle banner */
.mid{left:427px;top:228px;width:622px;height:79px}
.mid .headline{left:238px;top:10px;width:240px;font-size:24px}
.mid .btn{left:502px;top:10px;width:106px;height:58px;background:var(--cta-yellow);color:var(--cta-red);font-size:15px;border:2px solid var(--cta-orange)}
.mid .btn span{font-size:12px;color:var(--brand-blue)}

/* medium rectangle */
.rect{left:360px;top:413px;width:403px;height:336px}
.rect .headline{left:176px;top:22px;width:220px;font-size:31px}
.rect .btn{left:184px;top:196px;width:192px;height:86px;background:var(--cta-yellow);color:var(--deep-blue);font-size:27px;border:3px solid var(--cta-orange)}

/* small square */
.square{left:953px;top:413px;width:173px;height:168px}
.square .btn{left:6px;right:6px;top:82px;height:76px;background:var(--deep-blue);color:#fff;font-size:20px;border-radius:4px}
.square .btn span{font-size:16px}

/* tiny button */
.tiny{left:991px;top:660px;width:113px;height:91px;background:#111;border-radius:14px;border:2px solid #fff}
.tiny .btn{left:4px;right:4px;top:42px;height:44px;color:var(--cta-orange);font-size:15px}
.tiny .btn span{font-size:10px;color:#fff}
</style>
</head>
<body>

<!-- skyscraper -->
<section class="ad sky">
  <div class="logo" style="left:0;top:0;width:200px;height:150px">
    <span class="mark"></span><span class="wordmark" style="font-size:24px">Bug Helpers<br>Hub</span>
  </div>
  <p class="headline">Find local exterminators in your Area!</p>
  <div class="fill photo-person" role="img" aria-label="Startled woman covering her mouth" style="left:0;top:270px;width:200px;height:190px"></div>
  <p class="btn">FREE<span style="font-size:16px">EXTERMINATOR<br>QUOTE</span></p>
  <div class="fill photo-critters" role="img" aria-label="Cockroach, spider and rat" style="left:0;top:550px;width:200px;height:124px"></div>
  <p class="tagline">GET FAST, FREE<span>Exterminators Quotes</span></p>
  <div class="url-bar" style="left:0;bottom:0;width:200px;height:22px;font-size:10px">www.locatebughelpers.example</div>
</section>

<!-- leaderboard -->
<section class="ad leader">
  <div class="logo" style="left:0;top:0;width:160px;height:140px">
    <span class="wordmark" style="font-size:22px">Bug Helpers<br>Hub</span>
  </div>
  <div class="fill photo-critters" role="img" aria-label="Assorted insects and a spider" style="left:160px;top:0;width:295px;height:100px"></div>
  <div class="url-bar" style="left:160px;top:100px;width:295px;height:40px;font-size:15px">www.locatebughelpers.example</div>
  <div class="fill photo-person" role="img" aria-label="Startled woman covering her mouth" style="left:455px;top:0;width:130px;height:140px"></div>
  <div class="fill photo-critters" role="img" aria-label="Rat and ants" style="left:585px;top:0;width:250px;height:100px"></div>
  <div class="fill" style="left:848px;top:8px;width:70px;height:70px;border-radius:50%;background:var(--badge-gold)"></div>
  <div class="get-fast">GET FAST</div>
  <p class="btn free">FREE <span>Exterminator<br>Quotes</span></p>
</section>

<!-- middle banner -->
<section class="ad mid">
  <div class="logo" style="left:0;top:0;width:100px;height:75px">
    <span class="wordmark" style="font-size:16px">Bug Helpers<br>Hub</span>
  </div>
  <div class="fill" role="img" aria-label="Suburban house under blue sky" style="left:100px;top:0;width:130px;height:75px;background:linear-gradient(var(--photo-sky) 0 40%,#b9a68e 40% 70%,var(--lawn) 70%)"></div>
  <p class="headline">Find Local<small style="font-size:15px">EXTERMINATORS</small><small style="font-size:13px">in your Area</small></p>
  <p class="btn">GET FREE<span>Exterminator Quotes</span></p>
</section>

<!-- medium rectangle -->
<section class="ad rect">
  <div class="logo" style="left:0;top:0;width:170px;height:120px">
    <span class="mark"></span><span class="wordmark" style="font-size:24px">Bug Helpers<br>Hub</span>
  </div>
  <p class="headline">Find Local<small style="font-size:19px">EXTERMINATORS</small><small style="font-size:17px">in your Area</small></p>
  <div class="fill photo-person" role="img" aria-label="Startled woman" style="left:0;top:120px;width:150px;height:178px"></div>
  <div class="fill photo-critters" role="img" aria-label="Spider, rat and ants" style="left:150px;top:120px;width:249px;height:178px"></div>
  <p class="btn">GET A FREE<br>QUOTE NOW</p>
  <div class="url-bar" style="left:0;bottom:0;width:399px;height:34px;font-size:17px">www.locatebughelpers.example</div>
</section>

<!-- small square -->
<section class="ad square">
  <div class="logo" style="left:0;top:0;width:169px;height:76px">
    <span class="wordmark" style="font-size:19px">Bug Helpers<br>Hub</span>
  </div>
  <p class="btn">GET FREE<span>Exterminators<br>Quotes</span></p>
</section>

<!-- tiny button -->
<section class="ad tiny">
  <div class="logo" style="left:20px;top:6px;width:70px;height:34px;border-radius:4px">
    <span class="wordmark" style="font-size:10px">Bug Helpers<br>Hub</span>
  </div>
  <p class="btn">GET FREE<span>Exterminator</span>QUOTES</p>
</section>

</body>
</html>
```